Looking for a hot sauce label designed
Name: Copper Lantern Hot sauce
Graphic: dragon in pictures supplied and the flame bigger going out in front of the dragon or happy for you to design a dragon in a similar style
Text font: using the text supplied for the name of the product only
Colour: Black graphic and text on light brown paper
Style: sketch dragon and text - simple minimalistic design
Label size: 7cm height x 17cm width

Target Market(s)

To sell in bars and supermarkets

Font styles to use
Script

Colors

Designer to choose only greyscale colors for use in the design.

Requirements
Must have
• Name of product: Copper Lantern Hot Sauce
Batch No:
Business name and address
Best before date:
Nutrition Information Panel
Ingredients
Shake well before use
Keep refrigerated after opening
Australian made using 100% local ingredients
175ml
Room for a barcode
Nice to have
• Any changes you think will improve label design

```html
<!DOCTYPE html>
<html lang="en">
<head>
<meta charset="utf-8">
<title>Copper Lantern Hot Sauce Label</title>
<link href="https://fonts.googleapis.com/css2?family=Arimo:wght@400;700&family=Roboto+Condensed:wght@400&family=Shadows+Into+Light&display=swap" rel="stylesheet">
<style>
  :root {
    --paper: #d2ae80;
    --ink: #111111;
    --art-tone: #b98f5c;
    --art-edge: #c9a270;
  }
  html, body { margin: 0; padding: 0; overflow: hidden; }
  body { width: 1200px; height: 495px; background: var(--paper); }
  .label {
    position: relative; width: 1200px; height: 495px;
    background: var(--paper); color: var(--ink);
    font-family: "Arimo", Arial, sans-serif; overflow: hidden;
  }
  .panel {
    position: absolute; left: 33px; top: 44px; width: 321px; height: 419px;
    border: 1.5px solid var(--ink); box-sizing: border-box;
  }
  .panel-divider { position: absolute; left: 0; right: 0; top: 259px; border-top: 1.5px solid var(--ink); }
  .t { position: absolute; white-space: nowrap; line-height: 1; }
  .nip-title { font-weight: 700; font-size: 17px; left: 58px; top: 10px; }
  .meta { font-size: 17px; }
  .col-head { font-size: 17px; text-align: center; }
  .row { font-family: "Roboto Condensed", "Arial Narrow", sans-serif; font-size: 15.5px; }
  .caution { font-size: 16.5px; }
  .caution b { font-weight: 700; }

  .product-name {
    position: absolute; left: 515px; top: 22px; margin: 0; font-weight: 400;
    font-family: "Shadows Into Light", cursive; font-size: 76px; line-height: 1;
    white-space: nowrap; letter-spacing: 1px;
  }
  .product-sub {
    position: absolute; left: 600px; top: 112px;
    font-family: "Shadows Into Light", cursive; font-size: 64px; line-height: 1;
    letter-spacing: 8px; white-space: nowrap;
  }
  .illustration {
    position: absolute; left: 558px; top: 200px; width: 424px; height: 278px;
    border-radius: 46% 40% 30% 36%;
    background: radial-gradient(ellipse at 55% 50%, var(--art-tone) 0%, var(--art-edge) 70%, var(--paper) 100%);
  }
  .volume { position: absolute; left: 406px; top: 428px; font-size: 29px; line-height: 1; }
  .notes {
    position: absolute; left: 372px; top: 300px; width: 176px;
    font-size: 11.5px; line-height: 15px;
  }
  .notes p { margin: 0; }
  .notes .bb-line { display: inline-block; width: 70px; border-bottom: 1px solid var(--ink); }
  .notes .maker { margin-top: 5px; }
  .barcode-space {
    position: absolute; left: 996px; top: 398px; width: 120px; height: 72px;
    border: 1px dashed var(--ink); box-sizing: border-box;
  }
  .claim {
    position: absolute; left: 1133px; top: 257px;
    transform: rotate(-90deg); transform-origin: 0 0;
    font-size: 17.5px; line-height: 20px; white-space: nowrap; text-transform: uppercase;
  }
  .batch-box {
    position: absolute; left: 1137px; top: 267px; width: 35px; height: 203px;
    border: 1.5px solid var(--ink); box-sizing: border-box;
  }
  .batch-text {
    position: absolute; left: 7px; top: 195px;
    transform: rotate(-90deg); transform-origin: 0 0;
    font-size: 16px; line-height: 20px; white-space: nowrap;
  }
  .batch-line { display: inline-block; width: 90px; border-bottom: 1px solid var(--ink); vertical-align: middle; margin-left: 3px; }
</style>
</head>
<body>
<div class="label">
  <section class="panel" aria-label="Nutrition information and ingredients">
    <div class="t nip-title">NUTRITION INFORMATION</div>
    <div class="t meta" style="left:20px;top:38px;">Servings per package</div>
    <div class="t meta" style="left:218px;top:38px;">:&nbsp; 17.00</div>
    <div class="t meta" style="left:20px;top:58px;">Serving size</div>
    <div class="t meta" style="left:177px;top:58px;">:</div>
    <div class="t meta" style="left:222px;top:58px;">170.00m</div>
    <div class="t col-head" style="left:155px;top:78px;">Ave. per<br><span style="display:inline-block;margin-top:3px;">serve</span></div>
    <div class="t col-head" style="left:234px;top:78px;">Ave. per<br><span style="display:inline-block;margin-top:3px;">100ml</span></div>

    <div class="t row" style="left:20px;top:117px;">Energy</div>
    <div class="t row" style="left:168px;top:117px;">257g</div>
    <div class="t row" style="left:252px;top:117px;">151 KJ</div>
    <div class="t row" style="left:20px;top:137px;">Protein</div>
    <div class="t row" style="left:168px;top:137px;">1.5g</div>
    <div class="t row" style="left:252px;top:137px;">0.9g</div>
    <div class="t row" style="left:20px;top:157px;">Fat, Total</div>
    <div class="t row" style="left:168px;top:157px;">3.2g</div>
    <div class="t row" style="left:252px;top:157px;">1.9g</div>
    <div class="t row" style="left:27px;top:176px;">-saturated</div>
    <div class="t row" style="left:168px;top:176px;">0.5g</div>
    <div class="t row" style="left:252px;top:176px;">0.3g</div>
    <div class="t row" style="left:20px;top:196px;">Carbohydrate</div>
    <div class="t row" style="left:168px;top:196px;">4.3g</div>
    <div class="t row" style="left:252px;top:196px;">2.5g</div>
    <div class="t row" style="left:31px;top:216px;">-sugars</div>
    <div class="t row" style="left:168px;top:216px;">3.7g</div>
    <div class="t row" style="left:252px;top:216px;">2.2g</div>
    <div class="t row" style="left:20px;top:235px;">Sodium</div>
    <div class="t row" style="left:168px;top:235px;">262g</div>
    <div class="t row" style="left:252px;top:235px;">154mg</div>

    <div class="panel-divider"></div>

    <div class="t caution" style="left:19px;top:277px;"><b>CAUTION:</b></div>
    <div class="t caution" style="left:19px;top:297px;">• Keep out of reach of children</div>
    <div class="t caution" style="left:19px;top:317px;">• Keep away and out of eyes</div>
    <div class="t caution" style="left:19px;top:336px;"><b>INGREDIENTS:</b> Carrots, onion,</div>
    <div class="t caution" style="left:19px;top:356px;">Habanero, water, lime juice, garlic.</div>
    <div class="t caution" style="left:19px;top:375px;">white vinegar, vegetable oil, ginger.</div>
    <div class="t caution" style="left:19px;top:395px;">cilantro, salt, pepper</div>
  </section>

  <h1 class="product-name">Copper Lantern</h1>
  <div class="product-sub">Hot sauce</div>

  <div class="illustration" role="img" aria-label="Line-drawn sketch of a grinning sitting dragon breathing a large curling flame"></div>

  <div class="notes">
    <p>Shake well before use.</p>
    <p>Keep refrigerated after opening.</p>
    <p>Best before: <span class="bb-line"></span></p>
    <p class="maker">Copper Lantern Sauce Co.<br>12 Wattle Lane, Ballarat VIC 3350</p>
  </div>

  <div class="volume">175ml</div>

  <div class="barcode-space" aria-label="Space reserved for barcode"></div>

  <div class="claim">Made using 100% fresh<br>Australian produce</div>

  <div class="batch-box">
    <div class="batch-text">Batch No<span class="batch-line"></span></div>
  </div>
</div>
</body>
</html>
```